Update Business Card Design

I'm looking to update my business cards. Attached is a photo of the current design. I like the black side so that does not have to be update. The white side needs to be updated. I want the design to be modern and minimalistic.
I am a lawyer and my firm's website is www.brennoxlegalco.com (for reference).
My firm's logo has a horizontal version (which is on the black side of the card) and a vertical version (on the white side). I would prefer to keep the vertical version on the white side and horizontal version on the black side (the logo files are attached).

I am open to redesigning the black side also. I would like one side to have the horizontal logo and the other to have the vertical logo.

```html
<!DOCTYPE html>
<html lang="en">
<head>
<meta charset="utf-8">
<title>Brennox Legal Co. – Business Card</title>
<link rel="stylesheet" href="https://fonts.googleapis.com/css2?family=Montserrat:wght@400;500;700&display=swap">
<style>
  :root {
    --backdrop: #2b2b2b;
    --card: #050505;
    --accent: #16b4e3;
    --muted: #8a8a8a;
    --ink: #f2f2f2;
  }
  * { box-sizing: border-box; margin: 0; padding: 0; }
  html, body { width: 1200px; height: 875px; overflow: hidden; }
  body {
    background: var(--backdrop);
    font-family: "Montserrat", sans-serif;
    position: relative;
  }
  .card {
    position: absolute;
    width: 520px;
    height: 300px;
    background: var(--card);
    border-radius: 18px;
    box-shadow: 0 20px 40px rgba(0,0,0,.45);
  }
  .card--front { left: 60px; top: 110px; }
  .card--back { left: 620px; top: 465px; }

  /* horizontal lockup */
  .lockup-h {
    position: absolute;
    left: 0; right: 0; top: 0; bottom: 0;
    display: flex; align-items: center; justify-content: center; gap: 16px;
  }
  .brand-dot {
    width: 26px; height: 26px; border-radius: 50%;
    background: var(--accent);
  }
  .brand-name {
    color: var(--accent);
    font-weight: 500;
    letter-spacing: 3px;
    text-transform: uppercase;
  }
  .lockup-h .brand-name { font-size: 30px; }

  /* back side */
  .lockup-v {
    position: absolute;
    left: 30px; top: 0; bottom: 0; width: 190px;
    display: flex; flex-direction: column; align-items: center; justify-content: center; gap: 14px;
    text-align: center;
  }
  .lockup-v .brand-dot { width: 40px; height: 40px; }
  .lockup-v .brand-name { font-size: 18px; line-height: 1.4; letter-spacing: 2px; }
  .divider {
    position: absolute; left: 240px; top: 60px; width: 1.5px; height: 180px;
    background: var(--accent);
  }
  .contact {
    position: absolute; left: 262px; top: 58px;
    color: var(--ink); font-size: 12px; line-height: 1.45;
  }
  .person { font-size: 21px; font-weight: 700; line-height: 1.1; }
  .person .first { color: var(--muted); }
  .person .last { color: var(--accent); }
  .role { font-size: 12px; margin-bottom: 12px; }
  .address { margin-bottom: 10px; }
  .lines { list-style: none; }
  .lines li { display: flex; align-items: center; gap: 8px; }
  .lines svg { width: 11px; height: 11px; fill: var(--accent); flex: none; }
</style>
</head>
<body>
  <section class="card card--front" aria-label="Card front">
    <div class="lockup-h">
      <span class="brand-dot"></span>
      <span class="brand-name">Brennox Legal Co.</span>
    </div>
  </section>

  <section class="card card--back" aria-label="Card back">
    <div class="lockup-v">
      <span class="brand-dot"></span>
      <span class="brand-name">Brennox<br>Legal Co.</span>
    </div>
    <div class="divider"></div>
    <div class="contact">
      <p class="person"><span class="first">Darren</span> <span class="last">Holloway</span></p>
      <p class="role">Attorney at Law</p>
      <p class="address">815 W. Alder Street, Suite 310<br>Fairmont Hills, CA 90412</p>
      <ul class="lines">
        <li><svg viewBox="0 0 24 24"><path d="M6.6 10.8a15 15 0 006.6 6.6l2.2-2.2c.3-.3.7-.4 1-.2 1.1.4 2.3.6 3.6.6.6 0 1 .4 1 1V20c0 .6-.4 1-1 1A17 17 0 013 4c0-.6.4-1 1-1h3.5c.6 0 1 .4 1 1 0 1.3.2 2.5.6 3.6.1.3 0 .7-.2 1z"/></svg>555.713.2940</li>
        <li><svg viewBox="0 0 24 24"><path d="M4 8h16v12H4zM7 3h10v5H7zM8 12h3v2H8zm5 0h3v2h-3zm-5 4h3v2H8zm5 0h3v2h-3z"/></svg>555.870.7015</li>
        <li><svg viewBox="0 0 24 24"><path d="M6 3h12v5H6zM3 9h18v8h-3v4H6v-4H3zm5 6v4h8v-4z"/></svg>555.870.7028</li>
        <li><svg viewBox="0 0 24 24"><path d="M2 5h20v14H2zm2 2v.5l8 5 8-5V7z"/></svg>darren@BrennoxLegalCo.com</li>
      </ul>
    </div>
  </section>
</body>
</html>
```